Business Card Design Project

We are a distribution company providing goods to Latin America. We sell everything from Medical equipment, generic medicines, to carecliners. The logo that we use is attached. The logo can incorporate different colors other than black for versatility. The company name is Valdren Global Enterprises and/or VGE. The card will be printed using 1 or more of the following: Silk mounted and/or embossed. So if the design ideas could be made to incorporate that technique or any other unique techniques, it would be great. The target market is dialysis centers/doctors.

Basic Info for card:
Marna Dowell
Purchasing Manager
417-305-6184 direct
417-521-7790 fax
marna.dowell@valdrenvge.example
www.valdrenvge.example

Target Market(s)

Latin America

Industry/Entity Type

Business

Requirements
Nice to have
• The Front of the card should have the basic contact information with company name/logo. The back of the card could incorporate

```html
<!DOCTYPE html>
<html lang="en">
<head>
<meta charset="utf-8">
<title>Valdren Global Enterprises – Business Card</title>
<link rel="stylesheet" href="https://fonts.googleapis.com/css2?family=Arimo:wght@400&display=swap">
<style>
  :root {
    --backdrop: #000000;
    --card: #ffffff;
    --ink: #111111;
  }
  html, body {
    margin: 0;
    padding: 0;
    overflow: hidden;
  }
  body {
    width: 1200px;
    height: 900px;
    background: var(--backdrop);
    position: relative;
    font-family: "Arimo", Arial, sans-serif;
    color: var(--ink);
  }
  .business-card {
    position: absolute;
    left: 259px;
    top: 244px;
    width: 684px;
    height: 360px;
    background: var(--card);
    border-radius: 2px;
  }
  .brand-mark {
    position: absolute;
    left: 136px;
    top: 86px;
    width: 110px;
    height: 110px;
  }
  .company-name {
    position: absolute;
    left: 51px;
    top: 283px;
    margin: 0;
    font-size: 17px;
    font-weight: 400;
    word-spacing: 6px;
    white-space: nowrap;
  }
  .contact-block {
    position: absolute;
    left: 391px;
    top: 84px;
    font-size: 16px;
    line-height: 22px;
  }
  .contact-group {
    margin: 0 0 22px 0;
  }
  .contact-group p {
    margin: 0;
    white-space: nowrap;
  }
  .person-name {
    word-spacing: 4px;
  }
</style>
</head>
<body>
  <section class="business-card">
    <svg class="brand-mark" viewBox="0 0 110 110" aria-hidden="true">
      <circle cx="55" cy="55" r="55" fill="var(--ink)"/>
    </svg>
    <h1 class="company-name">Valdren Global Enterprises</h1>

    <div class="contact-block">
      <div class="contact-group">
        <p class="person-name">Marna Dowell</p>
        <p class="person-title">Purchasing Manager</p>
      </div>
      <div class="contact-group">
        <p class="phone-direct">417-305-6184 direct</p>
        <p class="phone-fax">417-521-7790 fax</p>
      </div>
      <div class="contact-group">
        <p class="email">marna.dowell@valdrenvge.example</p>
        <p class="website">www.valdrenvge.example</p>
      </div>
    </div>
  </section>
</body>
</html>
```